Nightclub promoter business cards

We need business cards designed for our company based in Port Elmsby, Avalonia called "NowMirazo". We are an events company that promotes weekly parties in the city. We cater to a 25+ crowd and feel like our brand should reflect that. We are looking for business cards that are textured and contain a unique design. We would prefer black cards. The final design should communicate the finest hospitality and prestige. I've attached files containing our logo. For more info. about our brand visit our website at www.nowmirazo.example.

Industry/Entity Type

Business

```html
<!DOCTYPE html>
<html lang="en">
<head>
<meta charset="utf-8">
<title>NowMirazo Business Cards</title>
<link href="https://fonts.googleapis.com/css2?family=Oswald:wght@600&family=Crimson+Text:ital@0;1&display=swap" rel="stylesheet">
<style>
  :root {
    --backdrop: #5b4838;
    --card: #f7f0d8;
    --band-fill: #c8c5b4;
    --ink: #1b1b18;
    --logo-ink: #4b4a44;
    --ornament: #e6dcc0;
    --shadow: rgba(0, 0, 0, 0.35);
  }
  html, body {
    margin: 0;
    padding: 0;
    overflow: hidden;
  }
  .canvas {
    position: relative;
    width: 1200px;
    height: 843px;
    background: var(--backdrop);
    overflow: hidden;
  }
  .card {
    position: absolute;
    top: 273px;
    width: 520px;
    height: 297px;
    background: var(--card);
    box-shadow: 0 10px 24px var(--shadow);
    overflow: hidden;
  }
  .card--back { left: 60px; }
  .card--front { left: 620px; }

  .band-block {
    position: absolute;
    background: var(--band-fill);
    border-left: 5px solid var(--ink);
    border-right: 5px solid var(--ink);
    box-sizing: border-box;
  }
  .rule-pair {
    position: absolute;
    height: 10px;
    border-top: 3px solid var(--ink);
    border-bottom: 3px solid var(--ink);
    box-sizing: border-box;
  }
  .wordmark {
    position: absolute;
    margin: 0;
    font-family: "Oswald", sans-serif;
    font-weight: 600;
    color: var(--logo-ink);
    letter-spacing: -1px;
    line-height: 1;
    white-space: nowrap;
  }
  .card--back .wordmark {
    left: 0;
    width: 100%;
    top: 116px;
    font-size: 54px;
    text-align: center;
  }
  .card--front .wordmark {
    left: 0;
    width: 100%;
    top: 62px;
    font-size: 46px;
    text-align: center;
  }
  .ornament {
    position: absolute;
    left: 175px;
    top: 118px;
    width: 180px;
    height: 44px;
    background: linear-gradient(90deg, transparent, var(--ornament) 20%, var(--ornament) 80%, transparent);
    border-radius: 22px;
  }
  .info {
    position: absolute;
    margin: 0;
    font-family: "Crimson Text", serif;
    color: var(--ink);
    line-height: 1.2;
  }
  .info--tagline { left: 0; width: 100%; top: 140px; text-align: center; font-size: 15px; }
  .info--city { left: 0; width: 100%; top: 183px; text-align: center; font-size: 11px; }
  .info--phone { left: 38px; top: 120px; font-size: 10px; font-style: italic; }
  .info--web { right: 40px; top: 240px; font-size: 11px; font-style: italic; text-align: right; }
</style>
</head>
<body>
  <main class="canvas">
    <section class="card card--back" aria-label="Card back">
      <div class="band-block" style="left:250px; top:0; width:110px; height:96px;"></div>
      <div class="rule-pair" style="left:250px; top:101px; width:110px;"></div>
      <h1 class="wordmark">nowmirazo</h1>
      <div class="rule-pair" style="left:250px; top:180px; width:110px;"></div>
      <div class="band-block" style="left:250px; top:195px; width:110px; height:102px;"></div>
    </section>

    <section class="card card--front" aria-label="Card front">
      <div class="band-block" style="left:290px; top:0; width:90px; height:50px;"></div>
      <h2 class="wordmark">nowmirazo</h2>
      <div class="ornament" role="img" aria-label="Decorative flourish beneath the company name"></div>
      <p class="info info--tagline">Company</p>
      <p class="info info--city">Port Elmsby, Avalonia</p>
      <p class="info info--phone">+1 555-014-2289</p>
      <div class="band-block" style="left:170px; top:225px; width:100px; height:72px;"></div>
      <p class="info info--web">www.nowmirazo.example<br>vip@nowmirazo.example</p>
    </section>
  </main>
</body>
</html>
```